I need a card to advertise my children's fun, factual television show for an international children's television conference in NYC. I will be pitching this show to QRN, TelZo, WMX, HVT, Rambling Atlas Youngsters and international production companies.

The show is about the different cultures you find in CANADA. It's called "Our Nearby Circle". It's about children, by children about celebrated holidays, cultural traditions and the uniqueness and similarities of all children in our country. The show's target audience are ages 6-9 (please research if you are not familiar with the age range). The show is educational so the card has to look super fun, exciting, colourful and playful to sell it. This is edutainment! Must be innovative and needs to be memorable to stand out.

you might want to check out: http://pupscreenhub.examplesite.net/gp/showsfortots58/lp/learnshows.htm
Updates

Please note that even though this is "postcard" design, it is NOT A POSTCARD. It's the size of a postcad but in the entertainment industry a "postcard" does not have a spot to address and mail.  It is a promotional card to hand out.Both sides of the card need to be designed.

Hello,

As requested by many I have made this project guaranteed and have extended the deadline 2 days (it's all I have!). Please review the project details prior to submission as I have further defined them.

I appreciate your creative talent and hard work on this and look forward to the results. I'm really hoping to stand out at this conference particularly since my subject matter is a harder sell to broadcasters. In order to sell it the broadcasters they have to be convinced that this is a fun, fast paced, exciting show and not just a boring and serious fact show. I'm looking to you to sell the idea with fun and colour, innovation, and spirit  but not miss the mark on the factual perspective. I will be pitching to QRN, Rambling Atlas Youngsters, WMX, HVT - take a look at the shows (age 6-9) they produce now - see what appeals to the broadcaster and keep that in mind as you design. This card may make the difference in whether this show is picked up or not!  I'm so looking forward to seeing your designs and working with you further refine it.

Thank you!

Target Market(s)

The cards target audience are social conscious broadcasters (QRN, WMX, HVT), mostly women ages 35-55. This card is required to sell the show to them so it must be fun, exciting and engaging.

Requirements
Must have
• Can anyone do this? I would like a card that is cut in the shape of an animated TV set that has a back pocket where you can place a two sided showcard giving the ability to change what appears on the TV. The insert showcard has on it the following information as well as the info in the attached files. When the showcard is out the back interior pocket has the colour bars. The back of the TV has a fold out stand. I need this completed on Jan 30 at the latest.

The insert card - must have (see attached - let me know if you can't open the files)
- Some photos could be: children of different races involved in doing something traditional; children active during Chinese New Year parade, Day of the Dead, Hunukkah, Diwali Festival, etc. the images are key
Nice to have
• Brainstorming: Ideally, I'd like this postcard to be flat and double layered - part of being memorable - Think sliding pictures with pull tabs, specialy cut paper. Innovative and smart. Perhaps there is a way to attach a giveaway, like Chinese Joss paper.
Should not have
• - The card should not have a place to address for mailing purposes. This is an entertainment industry version of a postcard. It's designed on both sides as promo material.
- It should not have common or uptight designs
- It should not have pictures of children in 3rd world countries. This is about the cultural diversity of children in a first world country - in my case Canada.

```html
<!DOCTYPE html>
<html lang="en">
<head>
<meta charset="utf-8">
<title>Our Nearby Circle – Promo Card</title>
<link rel="stylesheet" href="https://fonts.googleapis.com/css2?family=Comfortaa:wght@400;700&family=Sniglet:wght@800&display=swap">
<style>
  :root {
    --stage: #2b2d31;
    --sky-top: #3f78c2;
    --sky-mid: #8db8e6;
    --sky-low: #e6eef7;
    --card-blue: #2aa3dd;
    --frame-orange: #f3931f;
    --strip-orange: #f08a1c;
    --frame-purple: #8a5bb8;
    --ink-navy: #1b2f5c;
    --ink-purple: #6a3fa0;
    --paper: #ffffff;
    --link-blue: #3d7fc2;
  }
  * { box-sizing: border-box; margin: 0; padding: 0; }
  html, body { width: 1200px; height: 800px; overflow: hidden; }
  body {
    background: var(--stage);
    font-family: "Comfortaa", sans-serif;
    position: relative;
  }

  .card {
    position: absolute;
    width: 540px;
    height: 360px;
    top: 220px;
    overflow: hidden;
    box-shadow: 0 12px 30px rgba(0,0,0,.45);
  }

  .brand {
    display: flex; align-items: center; gap: 6px;
    font-family: "Comfortaa", sans-serif; font-weight: 700;
    color: var(--ink-purple); white-space: nowrap;
  }
  .brand__dot { border-radius: 50%; background: var(--frame-orange); flex: none; }

  /* Front */
  .card--front { left: 30px; background: var(--paper); }
  .front__photo {
    position: absolute; inset: 0 0 44px 0;
    background:
      radial-gradient(ellipse 38% 55% at 66% 92%, rgba(214,48,40,.85) 0%, rgba(214,48,40,.55) 45%, rgba(214,48,40,0) 100%),
      radial-gradient(ellipse 30% 45% at 52% 80%, rgba(38,82,170,.75) 0%, rgba(38,82,170,0) 100%),
      linear-gradient(180deg, var(--sky-top) 0%, var(--sky-mid) 45%, var(--sky-low) 100%);
  }
  .front__title {
    position: absolute; left: 40px; top: 86px;
    font-family: "Sniglet", sans-serif; font-weight: 800;
    font-size: 40px; line-height: 1.05; color: var(--paper);
    letter-spacing: 1px;
    transform: rotate(-4deg);
    text-shadow: 0 2px 3px rgba(30,50,90,.45);
  }
  .front__title .accent { color: var(--frame-orange); }
  .front__brand { position: absolute; right: 22px; top: 20px; font-size: 15px; }
  .front__brand .brand__dot { width: 14px; height: 14px; }
  .front__footer {
    position: absolute; left: 0; right: 0; bottom: 0; height: 44px;
    background: var(--paper);
    display: flex; align-items: center; justify-content: center;
    font-size: 13px; font-weight: 700; color: var(--link-blue);
  }

  /* Back */
  .card--back { left: 630px; background: linear-gradient(160deg, #35b0e8 0%, var(--card-blue) 60%, #2196d3 100%); }
  .back__strip {
    position: absolute; left: 0; right: 0; bottom: 0; height: 26px;
    background: var(--strip-orange);
  }
  .frame {
    position: absolute;
    border: 7px solid var(--frame-orange);
    box-shadow: 4px 4px 0 rgba(0,0,0,.18);
  }
  .frame--sunset {
    left: 26px; top: 16px; width: 124px; height: 86px;
    transform: rotate(-3deg);
    background:
      radial-gradient(circle at 50% 62%, #fff2a8 0%, #f9c940 30%, rgba(249,201,64,0) 60%),
      linear-gradient(180deg, #f4b23a 0%, #f08a1c 62%, #2a1c10 63%, #1e140b 100%);
  }
  .frame--hero {
    left: 26px; top: 152px; width: 168px; height: 108px;
    transform: rotate(2deg);
    border-left-color: var(--frame-purple);
    border-top-color: var(--frame-purple);
    background:
      radial-gradient(ellipse 40% 50% at 72% 80%, rgba(214,48,40,.9) 0%, rgba(214,48,40,0) 100%),
      radial-gradient(ellipse 25% 35% at 52% 62%, rgba(38,82,170,.8) 0%, rgba(38,82,170,0) 100%),
      linear-gradient(180deg, #7fb0e4 0%, #dbe8f5 100%);
  }
  .frame--jump {
    left: 318px; top: 188px; width: 184px; height: 110px;
    transform: rotate(-2deg);
    background:
      radial-gradient(ellipse 60% 40% at 50% 30%, #fff6dc 0%, rgba(255,246,220,0) 100%),
      linear-gradient(180deg, #f2e6c8 0%, #e2c99a 55%, #2b2620 72%, #1d1a16 100%);
  }
  .back__brand { position: absolute; right: 20px; top: 14px; font-size: 12px; }
  .back__brand .brand__dot { width: 11px; height: 11px; }
  .back__blurb {
    position: absolute; left: 200px; top: 38px; width: 318px;
    color: var(--ink-navy); font-size: 11px; line-height: 1.45; text-align: right;
  }
  .back__pitch {
    position: absolute; left: 26px; top: 110px;
    color: var(--frame-orange); font-weight: 700; font-size: 12px; line-height: 1.3;
  }
  .back__pitch .sub { color: var(--ink-navy); font-size: 9px; font-weight: 400; }
  .back__specs {
    position: absolute; left: 200px; top: 146px;
    color: var(--ink-navy); font-weight: 700; font-size: 10px;
  }
  .back__format {
    position: absolute; left: 26px; top: 270px;
    color: var(--paper); font-size: 9px; font-weight: 700;
  }
  .back__contact {
    position: absolute; left: 104px; bottom: 34px;
    display: flex; gap: 16px;
    color: var(--paper); font-size: 9px; font-weight: 700;
  }
  .back__ages {
    position: absolute; right: 22px; bottom: 5px;
    color: var(--paper); font-size: 12px; font-weight: 700;
  }
</style>
</head>
<body>

  <section class="card card--front" aria-label="Card front">
    <div class="front__photo" role="img" aria-label="Photo: child in a superhero mask and red cape reaching toward a bright blue sky"></div>
    <h1 class="front__title">Our <span class="accent">Nearby</span><br>Circle</h1>
    <div class="brand front__brand"><span class="brand__dot"></span>Tulip Frames Studio</div>
    <div class="front__footer">www.TulipFramesStudio.com</div>
  </section>

  <section class="card card--back" aria-label="Card back">
    <div class="frame frame--sunset" role="img" aria-label="Photo: children's silhouettes jumping against a sunset"></div>
    <div class="frame frame--hero" role="img" aria-label="Photo: child in a cape reaching up to the sky"></div>
    <div class="frame frame--jump" role="img" aria-label="Photo: silhouetted children leaping with a ball"></div>

    <div class="brand back__brand"><span class="brand__dot"></span>Tulip Frames Studio</div>

    <p class="back__blurb">Be a global explorer in your own neighbourhood. Go on an adventure with real kids who enlighten us on why there's a dragon in the Chinese parade, what happens on the Day of the Dead, and what the beast Krampus does to children at Christmas.</p>

    <p class="back__pitch">Edutainment Proposal<br><span class="sub">Fun Facts Series</span></p>
    <p class="back__specs">26 episodes x 11 minutes</p>
    <p class="back__format">live action format and animation</p>

    <div class="back__contact">
      <span>www.TulipFramesStudio.com</span>
      <span>604-555-0172</span>
    </div>

    <div class="back__strip"></div>
    <p class="back__ages">Ages 6-9</p>
  </section>

</body>
</html>
```